Medical Company in need of a Modern Flyer design for new Wound Care clinic.

Tri-Fold modern flyer design for our Woundcare company. Logo and description of services can be found on our website; https://www.corvin-woundcare.com/

```html
<!DOCTYPE html>
<html lang="en">
<head>
<meta charset="utf-8">
<title>Corvin Wound Care – Tri-Fold Flyer</title>
<link rel="stylesheet" href="https://fonts.googleapis.com/css2?family=Arimo:wght@400;700&family=Poppins:wght@400;500&family=Roboto:wght@700&display=swap">
<style>
  :root {
    --deep-teal: #06282a;
    --paper: #f7f7f7;
    --ink: #0b0b0b;
    --white: #ffffff;
    --gold: #c38f35;
    --gold-light: #e0b45e;
  }
  * { margin: 0; padding: 0; box-sizing: border-box; }
  html, body { width: 1200px; height: 927px; overflow: hidden; background: var(--white); }
  .flyer { position: relative; width: 1200px; height: 927px; overflow: hidden; font-family: "Arimo", Arial, sans-serif; }

  /* Left panel */
  .panel-about { position: absolute; left: 0; top: 0; width: 400px; height: 927px; }
  .about-block { position: absolute; left: 0; top: 0; width: 400px; height: 574px; background: var(--deep-teal); }
  .about-title { position: absolute; left: 67px; top: 66px; font: 700 38px/1 "Arimo", Arial, sans-serif; color: var(--white); }
  .about-text { position: absolute; left: 67px; top: 148px; width: 300px; font: 700 19.5px/23.7px "Arimo", Arial, sans-serif; color: var(--white); }
  .cross { position: absolute; }
  .cross-top { left: 322px; top: 64px; width: 64px; height: 64px; }
  .cross-bottom { left: 66px; top: 561px; width: 53px; height: 53px; z-index: 2; }
  .photo-surgeon-side { position: absolute; left: 0; top: 574px; width: 400px; height: 353px;
    background: radial-gradient(ellipse at 45% 55%, #5e9190 0%, #2f6766 45%, #163c3d 100%); }

  /* Middle panel */
  .panel-contact { position: absolute; left: 400px; top: 0; width: 400px; height: 927px; background: var(--paper); text-align: center; color: var(--ink); }
  .brand-name { position: absolute; left: 0; width: 400px; top: 200px; font: 400 28px/1 "Poppins", Arial, sans-serif; letter-spacing: 0.2em; padding-left: 0.2em; color: var(--ink); }
  .info-title { position: absolute; left: 0; width: 400px; top: 326px; font: 700 35px/1 "Roboto", Arial, sans-serif; }
  .contact-icon { position: absolute; left: 50%; transform: translateX(-50%); }
  .contact-line { position: absolute; left: 0; width: 400px; font: 400 20.5px/25px "Arimo", Arial, sans-serif; }

  /* Right panel */
  .panel-cover { position: absolute; left: 800px; top: 0; width: 400px; height: 927px; }
  .photo-surgeon-front { position: absolute; inset: 0;
    background: linear-gradient(180deg, #2a3231 0%, #313a39 40%, #2b5d72 70%, #1a4a5e 100%); }
  .cover-frame { position: absolute; left: -12px; top: 574px; width: 412px; height: 278px; background: var(--white); }
  .cover-box { position: absolute; left: 0; top: 574px; width: 400px; height: 260px; background: var(--deep-teal); }
  .cover-heading { position: absolute; left: 24px; top: 20px; font: 700 51px/77px "Arimo", Arial, sans-serif; color: var(--white); }
  .dot-grid { position: absolute; left: 327px; top: 14px; }
</style>
</head>
<body>
<div class="flyer">

  <section class="panel-about">
    <div class="about-block">
      <h2 class="about-title">About Us</h2>
      <svg class="cross cross-top" viewBox="0 0 64 64" aria-hidden="true">
        <path d="M22 3h20v19h19v20H42v19H22V42H3V22h19z" fill="none" stroke="var(--white)" stroke-width="5" stroke-linejoin="round"/>
      </svg>
      <p class="about-text">At Corvin Wound Care, we specialize in managing outpatient wound care facilities throughout the Dallas/Fort Worth area. Partnering with hospitals and local rehabilitation units, we deliver the most advanced wound care treatments. Our commitment to quality care resonates through our collaboration with small practice family providers, ensuring personalized, effective treatment plans.</p>
    </div>
    <div class="photo-surgeon-side" role="img" aria-label="Photo of a surgeon in a teal cap and mask, seen in profile during an operation"></div>
    <svg class="cross cross-bottom" viewBox="0 0 64 64" aria-hidden="true">
      <path d="M22 3h20v19h19v20H42v19H22V42H3V22h19z" fill="none" stroke="var(--white)" stroke-width="6" stroke-linejoin="round"/>
    </svg>
  </section>

  <section class="panel-contact">
    <div class="brand-name">CORVIN WOUNDCARE</div>
    <h2 class="info-title">More Information :</h2>

    <svg class="contact-icon" style="top:419px" width="54" height="38" viewBox="0 0 54 38" aria-hidden="true">
      <path d="M3 13c0-7 10-11 24-11s24 4 24 11v3h-12v-5H15v5H3z" fill="var(--gold)"/>
      <path d="M12 14h30l6 17v5H6v-5z" fill="var(--gold)"/>
      <circle cx="27" cy="24" r="8" fill="none" stroke="var(--paper)" stroke-width="1.5"/>
      <circle cx="27" cy="24" r="2.5" fill="var(--paper)"/>
      <rect x="19" y="32" width="16" height="2" fill="var(--paper)"/>
    </svg>
    <div class="contact-line" style="top:470px">+972-555-0147</div>

    <svg class="contact-icon" style="top:521px" width="50" height="50" viewBox="0 0 50 50" aria-hidden="true">
      <circle cx="25" cy="25" r="25" fill="var(--gold)"/>
      <rect x="16" y="10" width="18" height="12" fill="none" stroke="var(--paper)" stroke-width="1.6"/>
      <path d="M19 14h12M19 18h12" stroke="var(--paper)" stroke-width="1.4"/>
      <rect x="10" y="22" width="30" height="14" rx="3" fill="none" stroke="var(--paper)" stroke-width="1.6"/>
      <text x="25" y="33" text-anchor="middle" font-family="Arimo, Arial, sans-serif" font-size="9" font-weight="700" fill="var(--paper)">FAX</text>
    </svg>
    <div class="contact-line" style="top:583px">+972-555-0147</div>

    <svg class="contact-icon" style="top:631px" width="38" height="54" viewBox="0 0 38 54" aria-hidden="true">
      <path d="M19 1C9 1 1 9 1 19c0 12 18 34 18 34s18-22 18-34C37 9 29 1 19 1z" fill="var(--gold)"/>
      <circle cx="19" cy="18" r="6.5" fill="var(--paper)"/>
    </svg>
    <div class="contact-line" style="top:700px">2816 Harlow Rd Ste 200 PMB 410527<br>Dallas, TX 75204</div>

    <svg class="contact-icon" style="top:774px" width="47" height="47" viewBox="0 0 47 47" aria-hidden="true">
      <circle cx="23.5" cy="23.5" r="22" fill="var(--gold)"/>
      <g fill="none" stroke="var(--paper)" stroke-width="2.4">
        <ellipse cx="23.5" cy="23.5" rx="9" ry="22"/>
        <path d="M23.5 1.5v44M2 16h43M2 31h43"/>
      </g>
    </svg>
    <div class="contact-line" style="top:836px">www.corvin-woundcare.com</div>
  </section>

  <section class="panel-cover">
    <div class="photo-surgeon-front" role="img" aria-label="Photo of a surgeon wearing a patterned scrub cap, mask and magnifying loupes, looking down while operating"></div>
    <div class="cover-frame"></div>
    <div class="cover-box">
      <h1 class="cover-heading">Caring<br>for Your<br>Well-being</h1>
      <svg class="dot-grid" width="66" height="240" viewBox="0 0 66 240" aria-hidden="true" fill="var(--white)">
        <g>
          <circle cx="5" cy="5" r="4.5"/><circle cx="23" cy="5" r="4.5"/><circle cx="41" cy="5" r="4.5"/><circle cx="59" cy="5" r="4.5"/>
          <circle cx="5" cy="38" r="4.5"/><circle cx="23" cy="38" r="4.5"/><circle cx="41" cy="38" r="4.5"/><circle cx="59" cy="38" r="4.5"/>
          <circle cx="5" cy="71" r="4.5"/><circle cx="23" cy="71" r="4.5"/><circle cx="41" cy="71" r="4.5"/><circle cx="59" cy="71" r="4.5"/>
          <circle cx="5" cy="104" r="4.5"/><circle cx="23" cy="104" r="4.5"/><circle cx="41" cy="104" r="4.5"/><circle cx="59" cy="104" r="4.5"/>
          <circle cx="5" cy="137" r="4.5"/><circle cx="23" cy="137" r="4.5"/><circle cx="41" cy="137" r="4.5"/><circle cx="59" cy="137" r="4.5"/>
          <circle cx="5" cy="170" r="4.5"/><circle cx="23" cy="170" r="4.5"/><circle cx="41" cy="170" r="4.5"/><circle cx="59" cy="170" r="4.5"/>
          <circle cx="5" cy="203" r="4.5"/><circle cx="23" cy="203" r="4.5"/><circle cx="41" cy="203" r="4.5"/><circle cx="59" cy="203" r="4.5"/>
          <circle cx="5" cy="236" r="4.5"/><circle cx="23" cy="236" r="4.5"/><circle cx="41" cy="236" r="4.5"/><circle cx="59" cy="236" r="4.5"/>
        </g>
      </svg>
    </div>
  </section>

</div>
</body>
</html>
```